A 3d printing services company "The Velvet Forge" needs a clutter breaking business card design

The Velvet Forge is a 3d design, animation and printing services company. We are in the B2B and B2C space. www.velvetforge.com.sg
We have been in business for a year.
The logo is already done (the current file is attached).
We need a business card design which reflects the 3d printing and animations services of the company. A standard rectangular shape is not an option. The card can be die cut.
The card should have the colors of the logo and should have a high tech wow feel to it.
The front of the card should have my name, designation, cellphone email and website details. No need for an office address.
Name: Ranjeet Kulkarni
Designation: Founder Director
Cellphone (65)91748253
email: ranjeet@velvetforge.com.sg
website: www.velvetforge.com.sg
The back of the card should have the services we offer:
1. 3d Design and Modelling
2. 3d Animation
3. 3D Printing
The tag line is: "make your ideas real"
Am uploading the current business card files(back and front).
Target Market(s)
Business owners and C level managers in Marine, Healthcare industry
Industry/Entity Type
Printing
Contact Information for Business Card
Name: Ranjeet Kulkarni
Cellphone (65)91748253
2. 3d Animation
3. 3D Printing
Look and feel

```html
<!DOCTYPE html>
<html lang="en">
<head>
<meta charset="utf-8">
<title>The Velvet Forge – Business Card</title>
<link rel="stylesheet" href="https://fonts.googleapis.com/css2?family=Montserrat:wght@400;500;600;700&display=swap">
<style>
  :root {
    --backdrop: #e9e6e1;
    --card: #ffffff;
    --green: #4cae3f;
    --green-dark: #2e8f3a;
    --blue: #1e6bb4;
    --violet: #4a4fb0;
    --cyan: #1aa6dc;
    --ink: #2b2f3a;
    --brand: #3da844;
  }
  * { margin: 0; padding: 0; box-sizing: border-box; }
  html, body { width: 1200px; height: 905px; overflow: hidden; }
  body {
    background: var(--backdrop);
    font-family: "Montserrat", sans-serif;
    position: relative;
  }
  .card-wrap {
    position: absolute;
    width: 680px;
    height: 385px;
    filter: drop-shadow(0 10px 16px rgba(0,0,0,0.18));
  }
  .card-wrap--back { left: 70px; top: 55px; }
  .card-wrap--front { left: 450px; top: 470px; }
  .card {
    position: relative;
    width: 100%;
    height: 100%;
    background: var(--card);
    overflow: hidden;
    clip-path: polygon(46px 0, 100% 0, 100% calc(100% - 46px), calc(100% - 46px) 100%, 0 100%, 0 46px);
  }
  .card__shapes { position: absolute; inset: 0; width: 100%; height: 100%; }

  .brand {
    position: absolute;
    left: 44px;
    top: 60px;
    display: flex;
    align-items: center;
    gap: 14px;
  }
  .brand__dot {
    width: 58px; height: 58px;
    border-radius: 50%;
    background: var(--blue);
  }
  .brand__name {
    font-weight: 700;
    font-size: 30px;
    line-height: 1;
    color: var(--brand);
    width: 190px;
  }

  .back__web {
    position: absolute;
    left: 48px;
    top: 244px;
    color: #fff;
    font-size: 15px;
    font-weight: 500;
    letter-spacing: 3px;
  }
  .services {
    position: absolute;
    left: 48px;
    top: 306px;
    display: flex;
    gap: 22px;
    list-style: none;
    font-size: 13px;
    font-weight: 600;
    color: var(--ink);
  }
  .services li { display: flex; align-items: center; gap: 8px; }
  .services li::before {
    content: "";
    width: 8px; height: 8px;
    background: var(--green);
  }

  .front__tagline {
    position: absolute;
    left: 40px;
    top: 168px;
    color: #fff;
    font-size: 15px;
    font-weight: 500;
    letter-spacing: 1px;
    text-transform: uppercase;
  }
  .front__person {
    position: absolute;
    left: 438px;
    top: 78px;
    width: 200px;
    text-align: center;
    color: #dfe9f7;
  }
  .front__name {
    font-size: 22px;
    font-weight: 700;
    text-transform: uppercase;
    line-height: 1.05;
  }
  .front__role {
    font-size: 11px;
    font-weight: 500;
    letter-spacing: 1px;
    text-transform: uppercase;
    margin-top: 4px;
  }
  .contact {
    position: absolute;
    left: 44px;
    top: 236px;
    list-style: none;
    font-size: 12.5px;
    color: var(--ink);
  }
  .contact li {
    display: flex;
    align-items: center;
    gap: 9px;
    height: 27px;
  }
  .contact svg { width: 14px; height: 14px; fill: var(--ink); }
</style>
</head>
<body>

<div class="card-wrap card-wrap--back">
<section class="card card--back" aria-label="Card back">
  <svg class="card__shapes" viewBox="0 0 680 385" preserveAspectRatio="none">
    <defs>
      <linearGradient id="backPanel" x1="0" x2="1" y1="0" y2="0">
        <stop offset="0" stop-color="#0c2a5c"/>
        <stop offset="1" stop-color="#2277c0"/>
      </linearGradient>
      <linearGradient id="backBand" x1="0" x2="1">
        <stop offset="0" stop-color="var(--green-dark)"/>
        <stop offset="1" stop-color="var(--green)"/>
      </linearGradient>
    </defs>
    <rect class="back__band" x="0" y="225" width="420" height="50" fill="url(#backBand)"/>
    <polygon class="back__panel" points="395,158 680,158 680,282 350,282" fill="url(#backPanel)"/>
  </svg>
  <div class="brand">
    <span class="brand__dot"></span>
    <span class="brand__name">The Velvet Forge</span>
  </div>
  <p class="back__web">www.velvetforge.com.sg</p>
  <ul class="services">
    <li>3D Design and Modelling</li>
    <li>3D Animation</li>
    <li>3D Printing</li>
  </ul>
</section>
</div>

<div class="card-wrap card-wrap--front">
<section class="card card--front" aria-label="Card front">
  <svg class="card__shapes" viewBox="0 0 680 385" preserveAspectRatio="none">
    <defs>
      <linearGradient id="frontBand" x1="0" x2="1">
        <stop offset="0" stop-color="var(--violet)"/>
        <stop offset="1" stop-color="var(--cyan)"/>
      </linearGradient>
      <linearGradient id="frontPanel" x1="0" x2="1">
        <stop offset="0" stop-color="#0b2556"/>
        <stop offset="1" stop-color="#2a6fbb"/>
      </linearGradient>
    </defs>
    <rect class="front__band" x="0" y="152" width="420" height="50" fill="url(#frontBand)"/>
    <polygon class="front__panel" points="452,60 650,60 650,202 400,202" fill="url(#frontPanel)"/>
    <rect class="front__accent" x="650" y="60" width="30" height="60" fill="var(--green)"/>
  </svg>
  <div class="brand">
    <span class="brand__dot"></span>
    <span class="brand__name">The Velvet Forge</span>
  </div>
  <p class="front__tagline">Make your ideas real</p>
  <div class="front__person">
    <p class="front__name">Ranjeet Kulkarni</p>
    <p class="front__role">Founder Director</p>
  </div>
  <ul class="contact">
    <li>
      <svg viewBox="0 0 24 24" aria-hidden="true"><path d="M7 1h10a2 2 0 0 1 2 2v18a2 2 0 0 1-2 2H7a2 2 0 0 1-2-2V3a2 2 0 0 1 2-2zm0 3v14h10V4zm5 15.5a1 1 0 1 0 0 2 1 1 0 0 0 0-2z"/></svg>
      <span>(65)91748253</span>
    </li>
    <li>
      <svg viewBox="0 0 24 24" aria-hidden="true"><path d="M2 5h20v14H2zm2 2v.5l8 5 8-5V7zm0 2.8V17h16V9.8l-8 5z"/></svg>
      <span>ranjeet@velvetforge.com.sg</span>
    </li>
    <li>
      <svg viewBox="0 0 24 24" aria-hidden="true"><path d="M12 2a10 10 0 1 0 0 20 10 10 0 0 0 0-20zm0 2c.9 0 2.2 1.9 2.7 5H9.3C9.8 5.9 11.1 4 12 4zM4.3 11h3a16 16 0 0 0 0 2h-3a8 8 0 0 1 0-2zm5 0h5.4a14 14 0 0 1 0 2H9.3a14 14 0 0 1 0-2zm7.4 0h3a8 8 0 0 1 0 2h-3a16 16 0 0 0 0-2zM9.3 15h5.4c-.5 3.1-1.8 5-2.7 5s-2.2-1.9-2.7-5z"/></svg>
      <span>www.velvetforge.com.sg</span>
    </li>
  </ul>
</section>
</div>

</body>
</html>
```